Ciel doux

Hello,
I’m a designer sunglasses reatail Store owner in Montreal, Quebec.

Looking for something modern, fresh with a trendy appeal.

Will send my logo.
Thank you.

Store

```html
<!DOCTYPE html>
<html lang="fr">
<head>
<meta charset="utf-8">
<title>Ciel doux — Cartes professionnelles</title>
<link rel="stylesheet" href="https://fonts.googleapis.com/css2?family=Cinzel:wght@700;900&family=Niconne&family=Open+Sans:wght@700&display=swap">
<style>
  :root {
    --page: #ffffff;
    --silver-light: #f6f6f7;
    --silver-mid: #dcdcde;
    --silver-dark: #c4c4c7;
    --band-gray: #e2e2e4;
    --wine-bright: #c62c38;
    --wine: #8e1322;
    --wine-deep: #4a0006;
    --ink: #111111;
    --paper: #ffffff;
  }
  * { box-sizing: border-box; margin: 0; padding: 0; }
  html, body { width: 1030px; height: 1200px; overflow: hidden; background: var(--page); }
  .sheet { position: relative; width: 1030px; height: 1200px; }

  .card {
    position: absolute; left: 12px; width: 1006px; height: 575px;
    border-radius: 46px; overflow: hidden;
    background: radial-gradient(ellipse 60% 70% at 88% 20%, var(--silver-light), var(--silver-mid) 60%, var(--silver-dark));
  }
  .card--front { top: 6px; }
  .card--back { top: 618px; }

  .band-thin { position: absolute; left: 0; right: 0; background: linear-gradient(90deg, var(--wine-deep), var(--wine) 50%, var(--wine-deep)); }
  .band-gray { position: absolute; left: 0; right: 0; background: var(--band-gray); }
  .band-red {
    position: absolute; left: 0; right: 0; bottom: 0;
    background: radial-gradient(ellipse 45% 90% at 50% 25%, var(--wine-bright), var(--wine) 45%, var(--wine-deep) 90%);
  }

  .card--front .band-thin { top: 372px; height: 20px; }
  .card--front .band-gray { top: 392px; height: 26px; }
  .card--front .band-red { top: 418px; }

  .brand {
    position: absolute; left: 160px; top: 150px;
    display: flex; align-items: center; gap: 34px;
  }
  .brand-dot { width: 118px; height: 118px; border-radius: 50%; background: var(--wine); }
  .brand-name {
    font-family: "Cinzel", serif; font-weight: 900; font-size: 78px;
    color: var(--ink); letter-spacing: 2px; line-height: 1;
  }

  .card--back .band-thin { top: 316px; height: 12px; }
  .card--back .band-gray { top: 328px; height: 12px; }
  .card--back .band-red { top: 340px; }

  .person { position: absolute; right: 46px; top: 96px; text-align: right; }
  .person-name {
    font-family: "Cinzel", serif; font-weight: 900; font-size: 40px;
    color: var(--ink); font-variant: small-caps; letter-spacing: 1px; line-height: 1;
  }
  .person-title {
    font-family: "Niconne", cursive; font-size: 38px; color: var(--ink);
    margin-right: 14px; line-height: 1;
  }

  .tagline {
    position: absolute; left: 106px; top: 230px; width: 791px; height: 82px;
    background: var(--paper); display: flex; align-items: center; justify-content: center;
    font-family: "Open Sans", sans-serif; font-weight: 700; font-size: 26px;
    color: var(--ink); text-align: center; line-height: 1.3;
  }

  .swoosh { position: absolute; left: 0; bottom: 0; width: 1006px; height: 120px; }

  .info { position: absolute; color: var(--paper); text-align: center; font-family: "Niconne", cursive; }
  .info-heading { font-size: 34px; line-height: 1.1; display: inline-block; }
  .info--address .info-heading { border-bottom: 1px solid rgba(255,255,255,.7); }
  .info-line { font-size: 21px; line-height: 1.25; }
  .info--address { left: 8px; top: 352px; width: 240px; }
  .info--contact { right: 46px; top: 366px; width: 160px; }
  .info--contact .info-line { font-size: 27px; line-height: 1.1; }
</style>
</head>
<body>
<main class="sheet">
  <section class="card card--front" aria-label="Recto">
    <div class="brand">
      <span class="brand-dot"></span>
      <span class="brand-name">CIEL DOUX</span>
    </div>
    <div class="band-thin"></div>
    <div class="band-gray"></div>
    <div class="band-red"></div>
  </section>

  <section class="card card--back" aria-label="Verso">
    <div class="person">
      <p class="person-name">Name Here</p>
      <p class="person-title">Title</p>
    </div>
    <p class="tagline">Lorem ipsum dolor sit amet, consectetur<br>adipiscing elit. Quisque laoreet</p>
    <div class="band-thin"></div>
    <div class="band-gray"></div>
    <div class="band-red"></div>
    <svg class="swoosh" viewBox="0 0 1006 120" preserveAspectRatio="none" aria-hidden="true">
      <defs>
        <linearGradient id="swooshFill" x1="0" y1="0" x2="1" y2="0">
          <stop offset="0" stop-color="#d0343f"/>
          <stop offset="0.5" stop-color="#a31a28"/>
          <stop offset="1" stop-color="#5a0009" stop-opacity="0.6"/>
        </linearGradient>
      </defs>
      <path d="M60 120 C 200 50, 520 20, 1006 70 L1006 90 C 560 50, 260 70, 120 120 Z" fill="url(#swooshFill)"/>
      <path d="M110 120 C 300 70, 600 60, 1006 95 L1006 120 Z" fill="#7a0c18" opacity="0.55"/>
    </svg>
    <div class="info info--address">
      <p class="info-heading">Address</p>
      <p class="info-line">orem ipsum dolor sit amet,</p>
      <p class="info-line">consectetur adipiscing elit.</p>
      <p class="info-line">Quisque laoreet.</p>
    </div>
    <div class="info info--contact">
      <p class="info-heading">Contact</p>
      <p class="info-line">555-5544-256</p>
      <p class="info-line">555-6632-564</p>
    </div>
  </section>
</main>
</body>
</html>
```